Business Card Design

Quiet Fernlight - edgy, unique, ontrend clothing for girls 0-12.
I would like simple styling with white background and natural beige/brown font, similar to attached font.

Industry/Entity Type

Clothing

Contact Information for Business Card

Hi, I would like a very simple business card, white background with natural, beige, brown font, Quiet Fernlight. I design and sell clothes for girls 0-12 with a touch of bohemian styling. I would like "Quiet Fernlight" on front and on back -
www.quietfernlight.example.au
Colette Brennick,
0491558213,
colettebrennick@mailvale.example.au

```html
<!DOCTYPE html>
<html lang="en">
<head>
<meta charset="utf-8">
<title>Quiet Fernlight – Business Cards</title>
<link rel="stylesheet" href="https://fonts.googleapis.com/css2?family=Gelasio:wght@400&display=swap">
<style>
  :root {
    --stage: #eef1f1;
    --card: #ffffff;
    --beige: #c8b48e;
    --beige-soft: #efe8dc;
    --sea-light: #dfe8e8;
    --sea: #a9c3c6;
    --sand: #c9c3b8;
    --shadow: rgba(40, 50, 55, 0.28);
  }
  html, body {
    margin: 0;
    padding: 0;
    width: 1200px;
    height: 927px;
    overflow: hidden;
    background: var(--stage);
  }
  .canvas {
    position: relative;
    width: 1200px;
    height: 927px;
  }
  .card {
    position: absolute;
    background: var(--card);
    box-shadow: 4px 6px 12px var(--shadow);
    overflow: hidden;
  }
  .card--front {
    left: 40px;
    top: 50px;
    width: 670px;
    height: 405px;
  }
  .card--back {
    left: 458px;
    top: 476px;
    width: 685px;
    height: 410px;
  }
  .brand {
    position: absolute;
    left: 0;
    right: 0;
    top: 168px;
    margin: 0;
    text-align: center;
    font-family: "Gelasio", Georgia, serif;
    font-weight: 400;
    font-size: 50px;
    line-height: 60px;
    color: var(--beige);
  }
  .contact {
    position: absolute;
    left: 34px;
    top: 24px;
    margin: 0;
    padding: 0;
    list-style: none;
    font-family: "Gelasio", Georgia, serif;
    font-size: 22px;
    line-height: 38.5px;
    color: var(--beige);
    white-space: nowrap;
    z-index: 2;
  }
  .ornament {
    position: absolute;
    left: 0;
    bottom: 0;
    width: 200px;
    height: 220px;
    background: radial-gradient(circle at 40% 55%, var(--beige-soft) 0%, rgba(255,255,255,0) 70%);
  }
  .photo {
    position: absolute;
    right: 0;
    top: 0;
    width: 245px;
    height: 100%;
    background:
      linear-gradient(to right, var(--card) 0%, rgba(255,255,255,0) 25%),
      linear-gradient(to bottom, var(--sea-light) 0%, var(--sea) 45%, var(--sea-light) 65%, var(--sand) 100%);
  }
</style>
</head>
<body>
  <main class="canvas">
    <section class="card card--front">
      <h1 class="brand">Quiet Fernlight</h1>
    </section>

    <section class="card card--back">
      <ul class="contact">
        <li>Colette Brennick</li>
        <li>t: 0491558213</li>
        <li>e: colettebrennick@mailvale.example.au</li>
        <li>w: www.quietfernlight.example.au</li>
      </ul>
      <div class="ornament" role="img" aria-label="Large faint outline flower ornament in the corner"></div>
      <div class="photo" role="img" aria-label="Photograph of a child in a white dress walking barefoot along the shoreline at the beach"></div>
    </section>
  </main>
</body>
</html>
```